Killer business card for bowling event and marketing company

Rapid 'Q' Promotions is a sports marketing company that specializes in unique bowling events that provide return on investment for sponsors and memorable experiences for participants and spectators. We need a new business card that simultaneously communicates professionalism and fun. Our preferred colors are black and re

Target Market(s)

Executives in the marketing and sponsorship departments of companies, tourism executives, bowling center owners, and people who love to bowl.

Industry/Entity Type

Business

Contact Information for Business Card

Dean T Walsh
Rapid 'Q' Promotions
PO Box 47
Millbrook, Kestrel USA 22871
Email: deant@rapidqpromotions.com
Mobile: 1-555-518-3762

Requirements
Must have
• Our preferred colors are black and red.
Nice to have
• I am considering the use of the attached image for the back of the card.

```html
<!DOCTYPE html>
<html lang="en">
<head>
<meta charset="utf-8">
<title>Rapid 'Q' Promotions – Business Card</title>
<link href="https://fonts.googleapis.com/css2?family=Arimo:wght@400;700&display=swap" rel="stylesheet">
<style>
  :root {
    --red: #c8102e;
    --black: #111111;
    --charcoal: #262626;
    --white: #ffffff;
    --stage: #e9e9ea;
  }
  * { margin: 0; padding: 0; box-sizing: border-box; }
  html, body {
    width: 1200px; height: 675px; overflow: hidden;
    background: var(--stage);
    font-family: "Arimo", Arial, sans-serif;
  }
  .business-card {
    position: absolute; left: 150px; top: 80px;
    width: 900px; height: 514px;
    overflow: hidden;
    box-shadow: 0 6px 18px rgba(0,0,0,.18);
  }
  .card-shapes { position: absolute; inset: 0; }
  .brand-name {
    position: absolute; left: 44px; top: 182px; width: 192px;
    color: var(--red); font-weight: 700; font-size: 32px;
    letter-spacing: .5px; text-align: center; white-space: nowrap;
  }
  .person-name {
    position: absolute; right: 44px; top: 154px;
    color: var(--white); font-weight: 700; font-size: 28px;
    letter-spacing: .5px; text-transform: uppercase; white-space: nowrap;
  }
  .company-name {
    position: absolute; right: 34px; top: 206px;
    color: var(--white); font-weight: 700; font-size: 28px;
    letter-spacing: .5px; text-transform: uppercase; white-space: nowrap;
  }
  .company-name .accent { color: var(--red); }
  .contact-list {
    position: absolute; left: 40px; top: 340px;
    list-style: none;
  }
  .contact-item {
    display: flex; align-items: center; gap: 14px;
    color: var(--white); font-weight: 700; font-size: 17px;
    line-height: 1.15; margin-bottom: 20px; white-space: nowrap;
  }
  .contact-icon {
    width: 32px; height: 32px; border-radius: 6px;
    background: var(--red); flex: none;
    display: flex; align-items: center; justify-content: center;
  }
  .address-line {
    display: inline-block; text-transform: uppercase; text-align: right;
  }
  .address-line span { display: block; }
</style>
</head>
<body>
  <article class="business-card">
    <svg class="card-shapes" width="900" height="514" viewBox="0 0 900 514">
      <defs>
        <linearGradient id="alley-tones" x1="0" y1="0" x2="0.6" y2="1">
          <stop offset="0" stop-color="#6b6f86"/>
          <stop offset="0.3" stop-color="#9c3a3a"/>
          <stop offset="0.6" stop-color="#d8a24a"/>
          <stop offset="1" stop-color="#b44a3a"/>
        </linearGradient>
      </defs>
      <rect class="card-base" width="900" height="514" fill="var(--red)"/>
      <rect class="photo-area" role="img" aria-label="Bowling alley photo with lit lanes and pins"
            x="300" y="22" width="578" height="470" rx="44" fill="url(#alley-tones)"/>
      <rect class="photo-veil" x="300" y="22" width="578" height="470" rx="44" fill="#b9b9b9" opacity="0.55"/>
      <polygon class="name-band" points="590,150 878,150 878,196 560,196" fill="var(--red)"/>
      <polygon class="company-band" points="460,196 878,196 878,252 430,252" fill="var(--black)"/>
      <polygon class="band-tab" points="430,252 470,252 450,300 410,300" fill="var(--red)" opacity=".85"/>
      <polygon class="side-strip" points="0,0 330,0 330,280 0,280" fill="var(--charcoal)"/>
      <polygon class="main-dark" points="0,0 240,0 330,280 610,514 0,514" fill="var(--black)"/>
      <polygon class="lower-dark" points="0,280 330,280 610,514 0,514" fill="var(--black)"/>
      <polygon class="logo-plate" points="40,110 270,110 232,295 40,295" fill="var(--white)"/>
    </svg>

    <div class="brand-name">RAPID 'Q'</div>
    <div class="person-name">Dean T Walsh</div>
    <div class="company-name">Rapid <span class="accent">'Q'</span> Promotions</div>

    <ul class="contact-list">
      <li class="contact-item">
        <span class="contact-icon">
          <svg width="18" height="18" viewBox="0 0 24 24"><path fill="#fff" d="M6.6 10.8a15.1 15.1 0 006.6 6.6l2.2-2.2a1 1 0 011-.25 11.4 11.4 0 003.6.57 1 1 0 011 1V20a1 1 0 01-1 1A17 17 0 013 4a1 1 0 011-1h3.5a1 1 0 011 1c0 1.25.2 2.45.57 3.57a1 1 0 01-.25 1z"/></svg>
        </span>
        1-555-518-3762
      </li>
      <li class="contact-item">
        <span class="contact-icon">
          <svg width="18" height="18" viewBox="0 0 24 24"><rect x="3" y="6" width="18" height="12" fill="#fff"/><path d="M3 6l9 7 9-7" fill="none" stroke="var(--red)" stroke-width="1.8"/></svg>
        </span>
        deant@rapidqpromotions.com
      </li>
      <li class="contact-item">
        <span class="contact-icon">
          <svg width="18" height="18" viewBox="0 0 24 24"><path fill="#fff" d="M12 2a7 7 0 00-7 7c0 5 7 13 7 13s7-8 7-13a7 7 0 00-7-7zm0 9.5A2.5 2.5 0 1112 6.5a2.5 2.5 0 010 5z"/></svg>
        </span>
        <span class="address-line">Millbrook, Kestrel<span>USA 22871</span></span>
      </li>
    </ul>
  </article>
</body>
</html>
```